Letterhead and Envelopes design using existing logo. Logo can be found at tlventures.net

Use existing logo (attached) and incorporate in letterhead and envelope designs.

Current logo can be viewed at tlventures.net the web site reflect various parent and sub companies. Please see attached as well.

Target Market(s)

Other oil and gas operators.

Industry/Entity Type

Oil And Gas

Font styles to use
Sans Serif

Colors

Designer to choose colors to be used in the design.

Requirements
Must have
• Current logo and address
Nice to have
• Modern, contemporary approach yet incorporate existing traditional design.
• After design is selected for Ridgemont Caldera Holdings I will use similar design for Royalties, Exploration, Energy and Farms with different color schemes.

```html
<!DOCTYPE html>
<html lang="en">
<head>
<meta charset="utf-8">
<title>Ridgemont Caldera Holdings — Letterhead</title>
<link href="https://fonts.googleapis.com/css2?family=Roboto:wght@400;500&family=Montserrat:wght@400&display=swap" rel="stylesheet">
<style>
  :root {
    --backdrop: #e4e4e4;
    --paper: #f1f1f1;
    --ink-dark: #111111;
    --ink-text: #7a7a7a;
    --ink-footer: #555555;
    --brand-green: #6b9a3a;
    --signature-tone: #dfe6d6;
  }
  * { margin: 0; padding: 0; box-sizing: border-box; }
  html, body {
    width: 1200px; height: 866px; overflow: hidden;
    background: var(--backdrop);
  }
  .letterhead {
    position: absolute; left: 308px; top: 24px;
    width: 584px; height: 818px;
    background: var(--paper);
    font-family: "Roboto", Arial, sans-serif;
    color: var(--ink-text);
  }
  .brand-tab {
    position: absolute; left: 236px; top: 0;
    width: 113px; height: 64px;
    background: var(--ink-dark);
  }
  .brand-name {
    position: absolute; left: 0; right: 0; top: 96px;
    display: flex; justify-content: center; align-items: center; gap: 8px;
  }
  .brand-dot {
    width: 12px; height: 12px; border-radius: 50%;
    background: var(--brand-green);
  }
  .brand-name-text {
    font-size: 15px; font-weight: 500; letter-spacing: 1.5px;
    text-transform: uppercase; color: var(--ink-dark);
  }
  .recipient {
    position: absolute; left: 51px; top: 255px;
    font-size: 10.5px; line-height: 15.3px;
  }
  .letter-body {
    position: absolute; left: 51px; width: 485px;
    font-size: 10.5px; line-height: 15.3px;
    text-align: justify;
  }
  .letter-body.first { top: 346px; }
  .letter-body.second { top: 483px; }
  .signature {
    position: absolute; left: 51px; top: 557px;
    width: 112px; height: 74px;
    background: var(--signature-tone);
    border-radius: 4px;
  }
  .signatory-title {
    position: absolute; left: 51px; top: 651px;
    font-size: 10.5px;
  }
  .contact-bar {
    position: absolute; left: 55px; top: 752px;
    display: flex; align-items: center;
    font-family: "Montserrat", Arial, sans-serif;
    font-size: 10.2px; line-height: 12.5px;
    color: var(--ink-footer);
  }
  .contact-item { display: flex; align-items: center; gap: 9px; }
  .contact-icon { width: 22px; height: 22px; flex: none; }
  .contact-divider {
    width: 1.5px; height: 26px; background: var(--brand-green);
    margin: 0 24px 0 26px;
  }
</style>
</head>
<body>
  <main class="letterhead">
    <div class="brand-tab"></div>
    <div class="brand-name">
      <span class="brand-dot"></span>
      <span class="brand-name-text">Ridgemont Caldera Holdings</span>
    </div>

    <address class="recipient" style="font-style:normal">
      Dear Halvorsen<br>
      Kestrel Print Works Corporation<br>
      Department Design
    </address>

    <p class="letter-body first">Lorem ipsum dolor sit amet, consectetuer adipiscing elit. Aenean commodo ligula eget dolor. Aenean massa. Cum sociis natoque penatibus et magnis dis parturient montes, nascetur ridiculus mus. Donec quam felis, ultricies nec, pellentesque eu, pretium quis, sem. Nulla consequat massa quis enim. Donec pede justo, fringilla vel, aliquet nec, vulputate eget, arcu. In enim justo, rhoncus ut, imperdiet a, venenatis vitae, justo. Nullam dictum felis eu pede mollis pretium. Integer tincidunt. Cras dapibus. Vivamus elementum semper nisi.Nullam dictum felis eu pede mollis pretium. Integer tincidunt. Cras dapibus. Vivamus elementum semper nisi.felis eu pede mollis pretium. Integer tincidunt. Cras dapibus.</p>

    <p class="letter-body second">Quisque rutrum. Aenean imperdiet. Etiam ultricies nisi vel augue. Curabitur ullamcorper ultricies nisi. Nam eget dui. Etiam rhoncus. Maecenas tempus, tellus eget condimentum rhoncus, sem quam semper libero, sit amet adipiscing sem neque sed ipsum.felis pede mollis pretium. I am tincidunt. Cras dapibus.</p>

    <div class="signature" role="img" aria-label="Handwritten signature of the director in green ink"></div>
    <p class="signatory-title">Director/Excecutive Director</p>

    <footer class="contact-bar">
      <div class="contact-item">
        <svg class="contact-icon" viewBox="0 0 22 22" aria-hidden="true">
          <circle cx="11" cy="11" r="11" fill="var(--brand-green)"/>
          <path d="M7.2 5.8c.5-.4 1.1-.3 1.4.2l1.1 1.8c.3.5.2 1-.2 1.4l-.7.6c.7 1.5 1.8 2.7 3.3 3.4l.6-.7c.4-.4 1-.5 1.4-.2l1.8 1.1c.5.3.6.9.2 1.4l-.8 1c-.5.6-1.3.8-2 .5-3.2-1.3-5.6-3.7-6.9-6.9-.3-.7-.1-1.5.5-2z" fill="#fff"/>
        </svg>
        <span>555-014-2870<br>555-014-2870</span>
      </div>
      <span class="contact-divider"></span>
      <div class="contact-item">
        <svg class="contact-icon" viewBox="0 0 22 22" aria-hidden="true">
          <circle cx="11" cy="11" r="11" fill="var(--brand-green)"/>
          <rect x="5.5" y="7" width="11" height="8" rx="1" fill="#fff"/>
          <path d="M5.8 7.4 11 11.4l5.2-4" fill="none" stroke="var(--brand-green)" stroke-width="1.1"/>
        </svg>
        <span>info@tlventures.net<br>www.tlventures.net</span>
      </div>
      <span class="contact-divider"></span>
      <div class="contact-item">
        <svg class="contact-icon" viewBox="0 0 22 22" aria-hidden="true">
          <circle cx="11" cy="11" r="11" fill="var(--brand-green)"/>
          <path d="M11 5a4 4 0 0 0-4 4c0 3 4 7.5 4 7.5s4-4.5 4-7.5a4 4 0 0 0-4-4z" fill="#fff"/>
          <circle cx="11" cy="9" r="1.5" fill="var(--brand-green)"/>
        </svg>
        <span>PO Box 318 Westvale<br>Ardenne 40217</span>
      </div>
    </footer>
  </main>
</body>
</html>
```